Customer Journey Graphic

I want to graphic to describe a marketing framework I am teaching a course on

It a framework for growing a business
The idea is we
get customers to "take a Journey" through 7 steps
to deliver value to them

There are 4 major concepts that impact this journey - Game Plan, Business Model, "Inside out thinking' and Unique Competitive advantage
These concepts can make the journey faster, get more people to take it or make it more valuable

The stages are

- Target
- attract
- nurture
- convert
- maximise
- loyalty
- reactivation

I want to uses this framework as an overall;; 'explainer' fro my idea ,so it must looks very professional, and work well in presentations

I have included a rought 'sketch; of my thinking as an attachment

Business Owners

Business

Serif

• clear, get acroess the idea of a Journye over times, teh idea you can improve your results throught applying concpets of ' business model', "inside out thinking: , unique competitive advantage and game plane

```html
<!DOCTYPE html>
<html lang="en">
<head>
<meta charset="utf-8">
<title>Customer Journey Framework</title>
<link rel="stylesheet" href="https://fonts.googleapis.com/css2?family=Arimo:wght@400&display=swap">
<style>
  :root{
    --bg:#ffffff;
    --ink:#1f6274;
    --icon:#235f6e;
    --cyan:#29bfe0;
    --orange:#f28a22;
    --wave:#00a9ec;
    --button-edge:#b9bcc0;
  }
  html,body{margin:0;padding:0;overflow:hidden;background:var(--bg);}
  .canvas{position:relative;width:1200px;height:940px;overflow:hidden;background:var(--bg);}
  .diagram{position:absolute;left:0;top:0;width:1200px;height:940px;}
  .concept{position:absolute;margin:0;font-family:"Arimo",Arial,sans-serif;font-weight:400;font-size:29px;line-height:1;color:var(--ink);white-space:nowrap;}
  .concept--inside{left:104px;top:122px;}
  .concept--advantage{right:93px;top:122px;}
  .concept--gameplan{left:92px;top:783px;}
  .concept--model{right:86px;top:783px;}
  .leader{fill:none;stroke-width:3;stroke-dasharray:7 5;}
  .leader--cyan{stroke:var(--cyan);}
  .leader--orange{stroke:var(--orange);}
  .dot--cyan{fill:var(--cyan);}
  .dot--orange{fill:var(--orange);}
  .ring{fill:none;stroke-width:35;}
  .ring--cyan{stroke:var(--cyan);}
  .ring--orange{stroke:var(--orange);}
  .journey-path{fill:none;stroke:var(--wave);stroke-width:28;}
  .stage-button{fill:url(#buttonFace);stroke:var(--button-edge);stroke-width:1.5;}
  .icon{fill:var(--icon);stroke:none;}
  .icon-line{fill:none;stroke:var(--icon);stroke-linecap:round;stroke-linejoin:round;}
</style>
</head>
<body>
<main class="canvas">
  <svg class="diagram" viewBox="0 0 1402 1098" width="1200" height="940" role="img" aria-label="Seven-stage customer journey shaped by four concepts">
    <defs>
      <linearGradient id="buttonFace" x1="0" y1="0" x2="1" y2="1">
        <stop offset="0" stop-color="#d4d6d9"/>
        <stop offset="0.55" stop-color="#eeeff0"/>
        <stop offset="1" stop-color="#ffffff"/>
      </linearGradient>
    </defs>

    <!-- concept leaders -->
    <g class="leaders">
      <polyline class="leader leader--cyan" points="118,185 415,185 493,264"/>
      <circle class="dot--cyan" cx="493" cy="264" r="8"/>
      <polyline class="leader leader--orange" points="1300,185 1000,185 923,264"/>
      <circle class="dot--orange" cx="923" cy="264" r="8"/>
      <polyline class="leader leader--orange" points="118,903 418,903 493,824"/>
      <circle class="dot--orange" cx="493" cy="824" r="8"/>
      <polyline class="leader leader--cyan" points="1300,903 1000,903 925,824"/>
      <circle class="dot--cyan" cx="925" cy="824" r="8"/>
    </g>

    <!-- concept ring -->
    <g class="concept-ring">
      <path class="ring ring--cyan" d="M386 543 A321 321 0 0 1 707 222"/>
      <path class="ring ring--orange" d="M707 222 A321 321 0 0 1 1028 543"/>
      <path class="ring ring--cyan" d="M1028 543 A321 321 0 0 1 707 864"/>
      <path class="ring ring--orange" d="M707 864 A321 321 0 0 1 386 543"/>
      <polygon class="dot--orange" points="684,210 684,236 704,223"/>
      <polygon class="dot--cyan" points="998,444 1022,436 1015,458"/>
      <polygon class="dot--orange" points="731,852 731,878 711,865"/>
      <polygon class="dot--cyan" points="390,646 412,640 398,622"/>
    </g>

    <!-- journey wave -->
    <path class="journey-path" d="M92 548 A89 89 0 0 0 270 548 A89 89 0 0 1 447 548 A89 89 0 0 0 625 548 A89 89 0 0 1 803 548 A89 89 0 0 0 980 548 A89 89 0 0 1 1158 548 A89 89 0 0 0 1336 548"/>

    <!-- stage buttons -->
    <g class="stages">
      <circle class="stage-button" cx="181" cy="548" r="74"/>
      <circle class="stage-button" cx="358" cy="548" r="74"/>
      <circle class="stage-button" cx="536" cy="548" r="74"/>
      <circle class="stage-button" cx="714" cy="548" r="74"/>
      <circle class="stage-button" cx="891" cy="548" r="74"/>
      <circle class="stage-button" cx="1069" cy="548" r="74"/>
      <circle class="stage-button" cx="1247" cy="548" r="74"/>
    </g>

    <!-- target -->
    <g class="stage-icon stage-icon--target" transform="translate(181 548)">
      <circle class="icon-line" r="49" stroke-width="5"/>
      <circle class="icon-line" r="37" stroke-width="4"/>
      <path class="icon-line" stroke-width="5" d="M0 -37 V-25 M0 25 V37 M-37 0 H-25 M25 0 H37"/>
      <circle class="icon" cx="0" cy="-10" r="9"/>
      <path class="icon" d="M-17 18 Q-17 2 -5 1 L0 7 L5 1 Q17 2 17 18 Z"/>
    </g>

    <!-- magnet -->
    <g class="stage-icon stage-icon--attract" transform="translate(358 548)">
      <g transform="rotate(45)">
        <path class="icon-line" stroke-width="17" stroke-linecap="butt" d="M-24 22 V-6 A24 24 0 0 1 24 -6 V22"/>
        <rect class="icon" x="-33" y="26" width="18" height="12"/>
        <rect class="icon" x="15" y="26" width="18" height="12"/>
      </g>
      <polygon class="icon" points="-22,-2 -8,-2 -15,12 -2,12 -30,42 -20,20 -32,20"/>
    </g>

    <!-- hand with leaf -->
    <g class="stage-icon stage-icon--nurture" transform="translate(536 548)">
      <path class="icon" d="M-30 -10 Q-34 -30 -28 -32 Q-22 -32 -20 -14 L-18 -40 Q-16 -48 -10 -46 Q-6 -44 -7 -36 L-6 -48 Q-4 -54 2 -52 Q6 -50 5 -42 L7 -40 Q10 -46 15 -43 Q18 -40 16 -30 L14 -5 L25 -22 Q31 -28 35 -23 Q37 -19 33 -12 L18 20 Q12 36 8 52 L-16 52 Q-18 36 -26 22 Q-32 8 -30 -10 Z"/>
      <path fill="#e9eaec" d="M2 -8 Q-18 8 -12 32 Q-6 44 4 44 Q18 30 14 8 Q10 -2 2 -8 Z"/>
      <path class="icon-line" stroke-width="2.5" d="M1 42 Q4 20 2 -2 M2 24 L10 16 M2 14 L-6 6 M2 32 L-6 24"/>
    </g>

    <!-- gear -->
    <g class="stage-icon stage-icon--convert" transform="translate(714 548)">
      <g class="icon">
        <rect x="-10" y="-53" width="20" height="22"/>
        <rect x="-10" y="-53" width="20" height="22" transform="rotate(45)"/>
        <rect x="-10" y="-53" width="20" height="22" transform="rotate(90)"/>
        <rect x="-10" y="-53" width="20" height="22" transform="rotate(135)"/>
        <rect x="-10" y="-53" width="20" height="22" transform="rotate(180)"/>
        <rect x="-10" y="-53" width="20" height="22" transform="rotate(225)"/>
        <rect x="-10" y="-53" width="20" height="22" transform="rotate(270)"/>
        <rect x="-10" y="-53" width="20" height="22" transform="rotate(315)"/>
      </g>
      <circle class="icon-line" r="28" stroke-width="18"/>
    </g>

    <!-- bar chart -->
    <g class="stage-icon stage-icon--maximise" transform="translate(891 548)">
      <rect class="icon" x="-28" y="22" width="14" height="20"/>
      <rect class="icon" x="-7" y="8" width="14" height="34"/>
      <rect class="icon" x="14" y="0" width="14" height="42"/>
      <path class="icon-line" stroke-width="9" stroke-linecap="butt" d="M-22 -12 Q-20 4 -4 2 Q8 0 10 -26"/>
      <polygon class="icon" points="-4,-24 24,-24 10,-42"/>
    </g>

    <!-- loyalty cycle -->
    <g class="stage-icon stage-icon--loyalty" transform="translate(1069 548)">
      <g class="icon-line" stroke-width="9" stroke-linecap="butt">
        <path d="M-22 -28 A36 36 0 0 1 10 -35"/>
        <path d="M28 -22 A36 36 0 0 1 35 10"/>
        <path d="M22 28 A36 36 0 0 1 -10 35"/>
        <path d="M-28 22 A36 36 0 0 1 -35 -10"/>
      </g>
      <g class="icon">
        <polygon points="8,-48 8,-22 30,-36"/>
        <polygon points="48,8 22,8 36,30"/>
        <polygon points="-8,48 -8,22 -30,36"/>
        <polygon points="-48,-8 -22,-8 -36,-30"/>
      </g>
    </g>

    <!-- reactivation -->
    <g class="stage-icon stage-icon--reactivation" transform="translate(1247 548)">
      <path class="icon-line" stroke-width="10" stroke-linecap="butt" d="M-28 -28 A40 40 0 1 1 -40 4"/>
      <polygon class="icon" points="-42,-44 -14,-40 -38,-16"/>
    </g>
  </svg>

  <p class="concept concept--inside">Inside Out Thinking</p>
  <p class="concept concept--advantage">Unique Advantage</p>
  <p class="concept concept--gameplan">Gameplan</p>
  <p class="concept concept--model">Business Model</p>
</main>
</body>
</html>
```